Business card

I need a business card design for my consulting company in animal welfare for livestock. I like clean, crisp, simple.

One I imagined was double-sided:
side1: just my name and contact information
side2: silhouette of farm animals. Could be 3 (pig, cow, chicken) or all the species (pig, cow, chicken, duck, sheep, rabbit, etc) that continue the length of the card. I have attached an image of a silhouette style.

But, I am open to any concept.

```html
<!DOCTYPE html>
<html lang="en">
<head>
<meta charset="utf-8">
<title>Consulting Company – Business Card</title>
<link rel="stylesheet" href="https://fonts.googleapis.com/css2?family=Lato:wght@400&display=swap">
<style>
  :root {
    --backdrop: #2e2e30;
    --card: #f8f8f8;
    --brand-blue: #0b6699;
    --ink: #111111;
    --divider: #b5b5b5;
    --ground-shadow: rgba(0, 0, 0, 0.28);
  }
  * { box-sizing: border-box; margin: 0; padding: 0; }
  html, body {
    width: 1200px;
    height: 675px;
    overflow: hidden;
    background: var(--backdrop);
    font-family: "Lato", "Gill Sans", sans-serif;
  }
  .canvas {
    position: relative;
    width: 1200px;
    height: 675px;
  }
  .card {
    position: absolute;
    width: 493px;
    height: 296px;
    background: var(--card);
  }
  .card--front { left: 125px; top: 62px; }
  .card--back  { left: 658px; top: 271px; }

  .title-band {
    position: absolute;
    left: 0; top: 83px;
    width: 100%; height: 70px;
    background: var(--brand-blue);
    display: flex;
    align-items: center;
    justify-content: center;
  }
  .company-name {
    color: #ffffff;
    font-size: 23px;
    font-weight: 400;
    letter-spacing: 0.3px;
  }
  .address {
    position: absolute;
    left: 0; top: 229px;
    width: 100%;
    text-align: center;
    font-size: 12.5px;
    color: var(--ink);
  }
  .contact-row {
    position: absolute;
    left: 0; top: 259px;
    width: 100%;
    display: flex;
    justify-content: center;
    align-items: center;
    font-size: 12.5px;
    color: var(--ink);
  }
  .contact-item {
    display: flex;
    align-items: center;
    gap: 5px;
    padding: 0 5px;
    height: 20px;
  }
  .contact-item + .contact-item { border-left: 1px solid var(--divider); }
  .contact-item svg { width: 12px; height: 12px; fill: var(--ink); }

  .emblem {
    position: absolute;
    left: 141px; top: 43px;
    width: 196px; height: 196px;
    border: 5px solid var(--brand-blue);
    border-radius: 50%;
    display: flex;
    align-items: center;
    justify-content: center;
    text-align: center;
  }
  .emblem-name {
    color: var(--brand-blue);
    font-size: 18px;
    font-weight: 400;
    line-height: 1.3;
    letter-spacing: 0.5px;
  }
  .emblem-ground {
    position: absolute;
    left: 176px; top: 245px;
    width: 127px; height: 6px;
    border-radius: 50%;
    background: radial-gradient(ellipse at center, var(--ground-shadow) 0%, rgba(0,0,0,0) 70%);
  }
</style>
</head>
<body>
<main class="canvas">
  <section class="card card--front" aria-label="Card front">
    <div class="title-band">
      <h1 class="company-name">CONSULTING COMPANY</h1>
    </div>
    <p class="address">Address: Lorem ipsum dolor sit amet, consectetur adipiscing elit</p>
    <div class="contact-row">
      <span class="contact-item">
        <svg viewBox="0 0 12 12" aria-hidden="true"><circle cx="6" cy="3.2" r="2.7"/><path d="M1 12c0-3.2 2.2-5 5-5s5 1.8 5 5z"/></svg>
        +00000000000
      </span>
      <span class="contact-item">
        <svg viewBox="0 0 12 12" aria-hidden="true"><path d="M3.5 0h5a1 1 0 0 1 1 1v10a1 1 0 0 1-1 1h-5a1 1 0 0 1-1-1V1a1 1 0 0 1 1-1zm.5 1.5v4h4v-4zm0 5.5v1h1V7zm1.5 0v1h1V7zM7 7v1h1V7zM4 8.8v1h1v-1zm1.5 0v1h1v-1zm1.5 0v1h1v-1z"/></svg>
        +0000000000
      </span>
      <span class="contact-item">
        <svg viewBox="0 0 12 12" aria-hidden="true"><path d="M0.5 2h11v8h-11zm1 1v.3L6 6.6l4.5-3.3V3zm0 1.5V9h9V4.5L6 7.8z"/></svg>
        xyz@example.com
      </span>
    </div>
  </section>

  <section class="card card--back" aria-label="Card back">
    <div class="emblem">
      <span class="emblem-name">CONSULTING<br>COMPANY</span>
    </div>
    <div class="emblem-ground" aria-hidden="true"></div>
  </section>
</main>
</body>
</html>
```